iOS page Redesign

Need a page to be redesigned for the app. The app helps users find caregivers for Senior and Child. Note that text "Enter Booking Date" has to be removed and that line with date and time stays. If possible I would like a 24 hr turnaround on this task.

Target Market(s)

Families looking for child and senior care

Industry/Entity Type

Childcare

Requirements
Must have
• Colour as per the app screen shot and color scheme

```html
<!DOCTYPE html>
<html lang="en">
<head>
<meta charset="utf-8">
<title>Search Wren – Caregiver Search</title>
<link href="https://fonts.googleapis.com/css2?family=Mulish:wght@300;400;500&display=swap" rel="stylesheet">
<style>
  :root {
    --purple: #685a8f;
    --purple-text: #5d5185;
    --teal: #7bb8ab;
    --placeholder: #aaa6b6;
    --divider: #e6e4ec;
    --search-bg: #f2f2f4;
    --star-off: #cfcfd4;
    --white: #ffffff;
    --backdrop: #ecebf0;
  }
  * { box-sizing: border-box; margin: 0; padding: 0; }
  html, body {
    width: 1200px; height: 1200px; overflow: hidden;
    background: var(--backdrop);
    font-family: "Mulish", sans-serif;
  }
  .screen {
    position: absolute; left: 300px; top: 67px;
    width: 600px; height: 1066px;
    background: var(--white);
    overflow: hidden;
  }
  .app-header {
    background: var(--purple);
    height: 104px;
    color: var(--white);
    position: relative;
  }
  .status-bar {
    height: 32px; display: flex; align-items: center;
    justify-content: space-between; padding: 0 12px;
    font-size: 19px; font-weight: 500;
  }
  .status-bar .signal { display: flex; align-items: center; gap: 6px; }
  .status-bar .battery { display: flex; align-items: center; gap: 6px; }
  .status-bar .time { position: absolute; left: 0; right: 0; text-align: center; top: 5px; }
  .nav-title {
    position: absolute; left: 0; right: 0; top: 44px;
    text-align: center; font-size: 27px; font-weight: 400;
  }
  .nav-back { position: absolute; left: 22px; top: 58px; }

  .search-form { padding-left: 30px; }
  .form-row {
    height: 78px; display: flex; align-items: center;
    font-size: 25px; font-weight: 400;
  }
  .form-row .icon { width: 32px; flex: none; display: flex; justify-content: center; margin-right: 28px; }
  .field {
    flex: 1; height: 100%; display: flex; align-items: center;
    border-bottom: 1.5px solid var(--divider);
    color: var(--placeholder);
    margin-right: 36px;
  }
  .field.value { color: var(--purple-text); }
  .split { display: flex; flex: 1; height: 100%; gap: 30px; margin-right: 36px; }
  .split .field { margin-right: 0; }
  .form-row:last-child .field { border-bottom: none; }

  .search-button {
    display: block; width: 100%; height: 82px;
    background: var(--teal); color: var(--white);
    border: none; font-family: inherit; font-size: 27px; font-weight: 400;
    margin-top: 6px;
  }
  .search-bar {
    height: 70px; background: var(--search-bg);
    display: flex; align-items: center; padding-left: 30px;
  }
  .results-label {
    background: var(--search-bg);
    color: var(--placeholder); font-size: 21px;
    padding: 6px 0 18px 66px;
  }
  .result {
    height: 112px; display: flex; align-items: center;
    padding: 0 30px 0 52px; position: relative;
  }
  .result + .result::before {
    content: ""; position: absolute; left: 170px; right: 0; top: 0;
    border-top: 1.5px solid var(--divider);
  }
  .avatar {
    width: 84px; height: 84px; border-radius: 50%; flex: none;
    margin-right: 26px;
  }
  .avatar.a1 { background: radial-gradient(circle at 45% 40%, #f2d9b8, #c9a27a); }
  .avatar.a2 { background: radial-gradient(circle at 45% 45%, #d9a98a, #3a8f93); }
  .avatar.a3 { background: radial-gradient(circle at 45% 45%, #c9b9b4, #2b2b30); }
  .caregiver { flex: 1; }
  .caregiver .name { color: var(--purple-text); font-size: 27px; }
  .stars { display: flex; gap: 3px; margin-top: 4px; }
  .rate { color: var(--purple-text); font-size: 25px; align-self: flex-start; margin-top: 18px; }
</style>
</head>
<body>
<main class="screen">
  <header class="app-header">
    <div class="status-bar">
      <span class="signal">
        <svg width="64" height="10" viewBox="0 0 64 10" fill="#fff"><circle cx="5" cy="5" r="4.5"/><circle cx="17" cy="5" r="4.5"/><circle cx="29" cy="5" r="4.5"/><circle cx="41" cy="5" r="4.5"/><circle cx="53" cy="5" r="4.5"/></svg>
        <svg width="20" height="15" viewBox="0 0 20 15" fill="none" stroke="#fff" stroke-width="2"><path d="M1 5a13 13 0 0 1 18 0"/><path d="M4.5 8.5a8 8 0 0 1 11 0"/><circle cx="10" cy="12.5" r="1.6" fill="#fff" stroke="none"/></svg>
      </span>
      <span class="time">9:41 AM</span>
      <span class="battery">100%
        <svg width="40" height="18" viewBox="0 0 40 18"><rect x="1" y="1" width="34" height="16" rx="3" fill="none" stroke="#fff" stroke-width="1.5"/><rect x="3" y="3" width="30" height="12" rx="1.5" fill="#fff"/><rect x="36.5" y="6" width="2.5" height="6" rx="1" fill="#fff"/></svg>
      </span>
    </div>
    <svg class="nav-back" width="22" height="36" viewBox="0 0 22 36" fill="none" stroke="#fff" stroke-width="3.5" stroke-linecap="round" stroke-linejoin="round"><path d="M19 3 4 18l15 15"/></svg>
    <h1 class="nav-title">Search Wren</h1>
  </header>

  <form class="search-form">
    <div class="form-row">
      <span class="icon">
        <svg width="28" height="28" viewBox="0 0 28 28" fill="var(--purple)"><circle cx="14" cy="8" r="6.5"/><path d="M1 27c0-7 6-10 13-10s13 3 13 10z"/></svg>
      </span>
      <span class="field">Caregiver Name (optional)</span>
    </div>
    <div class="form-row">
      <span class="icon">
        <svg width="26" height="34" viewBox="0 0 26 34" fill="var(--purple)"><path d="M13 0a10 10 0 0 0-10 10c0 7.5 10 17 10 17s10-9.5 10-17A10 10 0 0 0 13 0zm0 14a4 4 0 1 1 0-8 4 4 0 0 1 0 8z"/><rect x="1" y="30" width="24" height="3" rx="1.5"/></svg>
      </span>
      <span class="field">Job Address (other than home address)</span>
    </div>
    <div class="form-row">
      <span class="icon">
        <svg width="30" height="30" viewBox="0 0 30 30" fill="none" stroke="var(--purple)" stroke-width="3"><rect x="2" y="5" width="26" height="23" rx="2"/><path d="M2 11h26M8 1v7M22 1v7"/><rect x="17" y="16" width="6" height="6" fill="var(--purple)" stroke="none"/></svg>
      </span>
      <div class="split">
        <span class="field value">09/12 09:00AM</span>
        <span class="field value">09/12 09:30AM</span>
      </div>
    </div>
    <div class="form-row">
      <span class="icon">
        <svg width="30" height="32" viewBox="0 0 30 32" fill="var(--purple)"><path d="M2 6h26a2 2 0 0 1 2 2v22a2 2 0 0 1-2 2H2a2 2 0 0 1-2-2V8a2 2 0 0 1 2-2z"/><rect x="10" y="1" width="10" height="8" rx="2" fill="var(--purple)" stroke="#fff" stroke-width="2"/><circle cx="15" cy="16" r="4.5" fill="#fff"/><path d="M6 28c0-5 4-7 9-7s9 2 9 7z" fill="#fff"/></svg>
      </span>
      <div class="split">
        <span class="field">Senior Care</span>
        <span class="field value">Child Care</span>
      </div>
    </div>
    <button type="button" class="search-button">Search</button>
  </form>

  <div class="search-bar">
    <svg width="32" height="32" viewBox="0 0 32 32" fill="none" stroke="var(--teal)" stroke-width="4" stroke-linecap="round"><circle cx="13" cy="13" r="9"/><path d="m20 20 9 9"/></svg>
  </div>
  <p class="results-label">Results</p>

  <section class="results">
    <article class="result">
      <div class="avatar a1" role="img" aria-label="Profile photo of caregiver Clara Whitmore"></div>
      <div class="caregiver">
        <p class="name">Clara Whitmore</p>
        <div class="stars">
          <svg width="150" height="26" viewBox="0 0 150 26"><g fill="var(--teal)"><path id="s" d="M13 1l3.5 8 8.5.7-6.5 5.6 2 8.4L13 19.3 5.5 23.7l2-8.4L1 9.7 9.5 9z"/><use href="#s" x="30"/><use href="#s" x="60"/><use href="#s" x="90"/><use href="#s" x="120"/></g></svg>
        </div>
      </div>
      <span class="rate">$125/hr</span>
    </article>
    <article class="result">
      <div class="avatar a2" role="img" aria-label="Profile photo of caregiver Nora Bellamy"></div>
      <div class="caregiver">
        <p class="name">Nora Bellamy</p>
        <div class="stars">
          <svg width="150" height="26" viewBox="0 0 150 26"><g fill="var(--teal)"><use href="#s"/><use href="#s" x="30"/><use href="#s" x="60"/><use href="#s" x="90"/></g><use href="#s" x="120" fill="var(--star-off)"/></svg>
        </div>
      </div>
      <span class="rate">$36/hr</span>
    </article>
    <article class="result">
      <div class="avatar a3" role="img" aria-label="Profile photo of caregiver Ada Fairfield"></div>
      <div class="caregiver">
        <p class="name">Ada Fairfield</p>
        <div class="stars">
          <svg width="150" height="26" viewBox="0 0 150 26"><g fill="var(--teal)"><use href="#s"/><use href="#s" x="30"/><use href="#s" x="60"/></g><g fill="var(--star-off)"><use href="#s" x="90"/><use href="#s" x="120"/></g></svg>
        </div>
      </div>
      <span class="rate">$48/hr</span>
    </article>
  </section>
</main>
</body>
</html>
```